Verdant Loop Advisors, LLC

I am looking for a simple, clear layout with my logo prominent and embossed, on the best quality card stock available. I would like the business name and phone number included on the card as well......I dont want my name anywhere on the card and I would like my logo embossed on the card......something simple with a white back......open to designs as long as they go along with recycling symbols and green type stuff.....The address, website, cell number, fax number, and email are listed below

5374 Tillbury Fenwood Road
Larkmoor, MD 20999

c. 240.555.0143 f. 240.555.0187
e. sales@verdantloopadvisors.example
w. www.verdantloopadvisors.example

Industry/Entity Type

Recycling

```html
<!DOCTYPE html>
<html lang="en">
<head>
<meta charset="utf-8">
<title>Verdant Loop Advisors, LLC — Business Card</title>
<link rel="stylesheet" href="https://fonts.googleapis.com/css2?family=Lato:wght@400;700&display=swap">
<style>
  :root {
    --page-bg: #e7eae4;
    --card-top: #f1f5ea;
    --card-top-edge: #dfe8d2;
    --brand-green: #2f8a47;
    --brand-green-dark: #1f6a33;
    --ink: #141414;
    --panel-black: #060606;
    --contact-text: #e4e4e4;
    --white: #ffffff;
  }
  * { box-sizing: border-box; margin: 0; padding: 0; }
  html, body {
    width: 1200px;
    height: 732px;
    overflow: hidden;
    background: var(--page-bg);
    font-family: "Lato", sans-serif;
  }
  .canvas {
    position: relative;
    width: 1200px;
    height: 732px;
  }
  .card {
    position: absolute;
    left: 180px;
    top: 126px;
    width: 840px;
    height: 480px;
    display: flex;
    flex-direction: column;
    box-shadow: 0 10px 30px rgba(0, 0, 0, 0.18);
    overflow: hidden;
  }
  .card-brand {
    height: 231px;
    background: linear-gradient(180deg, var(--card-top) 0%, var(--card-top-edge) 100%);
    display: flex;
    align-items: center;
    padding-left: 81px;
    gap: 26px;
  }
  .brand-mark {
    width: 78px;
    height: 78px;
    border-radius: 50%;
    background: var(--brand-green);
    flex-shrink: 0;
  }
  .brand-name {
    font-weight: 700;
    font-size: 44px;
    letter-spacing: 1px;
    color: var(--ink);
    white-space: nowrap;
  }
  .card-address {
    height: 55px;
    background: linear-gradient(180deg, var(--brand-green) 0%, var(--brand-green-dark) 100%);
    display: flex;
    align-items: center;
    padding-left: 112px;
    gap: 26px;
    color: var(--white);
    font-size: 22px;
    white-space: nowrap;
  }
  .card-contacts {
    flex: 1;
    background: var(--panel-black);
    display: grid;
    grid-template-columns: 248px auto;
    grid-auto-rows: 30px;
    align-content: start;
    padding: 46px 0 0 118px;
    color: var(--contact-text);
    font-size: 20px;
    letter-spacing: 0.5px;
  }
  .contact-item {
    display: flex;
    align-items: center;
    gap: 14px;
    white-space: nowrap;
  }
  .contact-icon {
    width: 18px;
    height: 18px;
    fill: var(--contact-text);
    flex-shrink: 0;
  }
  .pin-icon { width: 26px; height: 32px; flex-shrink: 0; }
</style>
</head>
<body>
<main class="canvas">
  <section class="card" aria-label="Verdant Loop Advisors business card">
    <header class="card-brand">
      <span class="brand-mark"></span>
      <h1 class="brand-name">Verdant Loop Advisors, LLC</h1>
    </header>

    <div class="card-address">
      <svg class="pin-icon" viewBox="0 0 26 32" aria-hidden="true">
        <path d="M13 1C6.9 1 2 5.8 2 11.8 2 19.6 13 31 13 31s11-11.4 11-19.2C24 5.8 19.1 1 13 1z" fill="#ffffff"/>
        <circle cx="13" cy="12" r="4.5" fill="#2f8a47"/>
      </svg>
      <span>5374 Tillbury Fenwood Road, Larkmoor, MD 20999</span>
    </div>

    <div class="card-contacts">
      <div class="contact-item">
        <svg class="contact-icon" viewBox="0 0 18 18" aria-hidden="true">
          <path d="M2 6c0-2 3-4 7-4s7 2 7 4v1.5h-4V5.5H6v2H2z"/>
          <path d="M4 9h10l1.5 6.5h-13z"/>
        </svg>
        <span>240 . 555 . 0143</span>
      </div>
      <div class="contact-item">
        <svg class="contact-icon" viewBox="0 0 18 18" aria-hidden="true">
          <path d="M2 3h14v12H2z M3.5 4.5v.6L9 9.2l5.5-4.1v-.6z" fill-rule="evenodd"/>
        </svg>
        <span>sales@verdantloopadvisors.example</span>
      </div>
      <div class="contact-item">
        <svg class="contact-icon" viewBox="0 0 18 18" aria-hidden="true">
          <path d="M5 2h8v4H5z"/>
          <path d="M1 7h16v7h-3v-2H4v2H1z"/>
          <path d="M5 13h8v3H5z"/>
        </svg>
        <span>240 . 555 . 0187</span>
      </div>
      <div class="contact-item">
        <svg class="contact-icon" viewBox="0 0 18 18" aria-hidden="true">
          <path d="M1 3h16v10H1z M2.6 4.6v6.8h12.8V4.6z" fill-rule="evenodd"/>
          <path d="M6 15h6v1.5H6z"/>
        </svg>
        <span>www.verdantloopadvisors.example</span>
      </div>
    </div>
  </section>
</main>
</body>
</html>
```